Hardcore nerd needs to stand out in a sea of dull Defence business cards

Wombat Devices is a new Australian consulting engineering company that turns research and theory into practical systems. No evangelistic fluff, just mathematics and physics into electronic and optical circuits for consumer products, scientific research or Defence applications.

We already have a recognised logo (provided) which is often dark blue/black on a light background but we're open to other combinations. (Us engineers tend to have limited aesthetic imagination :)

Some of our recent products have included:
* Instrumentation for electrical testing,
* Radar jammers,
* GPS antenna design,
* Satellite tracking systems,
* High power lasers

We're open to both single and double-sided designs - happy to be convinced either way.

P.S. Another group is working on the web page, so - alas - our web site is currently of no use for images/ideas...

Target Market(s)

Engineering managers,
Scientists

Contact Information for Business Card

Dr Colin Marsh
R&D Engineer

colin@wombatdevicesco.com.au
0427 563 210

PO Box XXX (to be confirmed)
Banks ACT 2913
Australia

Font styles to use
Serif
Sans Serif

Colors

Designer to choose colors to be used in the design.

Requirements
Must have
• My contact details!
• I've had many (great) "bold and plain" designs submitted already, so feel free to be artistically creative :)
• Happy to take advice re fonts/colours/printability etc.
Nice to have
• I'm not sure if "lists" are more at home on a CV than a business card, but representative services include:
• Applied electromagnetics
• RF and high speed electronics
• Signal and image processing
• Electro-optical and laser systems
• Concept-to-prototype design services
• If you're considering double sided cards, then often measuring/alignment grids/rulers feature on the back of similar cards.
• e.g. https://www.lumoptix-example.com/newgrouppage9.cfm?objectgroup_id=4815
• https://www.lumoptix-example.com/newgrouppage9.cfm?objectgroup_ID=4817
• ..or even a "Smith chart" (google will return lots)
• Generic images to represent a capability might work - googling images associated with keyword for each of these areas might help:
• - "passive radar", "phased array", "fdtd", "vircator"
• RF and high speed electronic design
• - "smith chart", "microstrip circuits", "dimensioned drawing", "electronic schematic"
• - "dft", "iir filter"
• - "optical cavity". "laser energy level diagram"
• Background/watermarked images outlines/wireframes/schematics would probably look OK.
Should not have
• If a list of projects/services is provided, it is important not to make the client feel that this is "all" the company can do. Engineering design is a creative discipline (like graphics :)
• Please, no stock "military" snaps like planes, missiles, etc!

```html
<!DOCTYPE html>
<html lang="en">
<head>
<meta charset="utf-8">
<title>Wombat Devices – Business Card</title>
<link rel="stylesheet" href="https://fonts.googleapis.com/css2?family=Libre+Baskerville:wght@400;700&display=swap">
<style>
  :root {
    --page-bg: #d9d6d1;
    --card-black: #0a0a0a;
    --card-grey: #4b4b4b;
    --brand-dim: #5c5c5c;
    --brand-dark: #0a0a0a;
    --text-light: #f2f2f2;
    --text-soft: #c9c9c9;
    --serif: "Libre Baskerville", Georgia, serif;
  }
  * { box-sizing: border-box; margin: 0; padding: 0; }
  html, body { width: 1200px; height: 800px; overflow: hidden; }
  body {
    background: var(--page-bg);
    font-family: var(--serif);
    position: relative;
  }
  .card {
    position: absolute;
    top: 245px;
    width: 540px;
    height: 309px;
    background: var(--card-black);
    overflow: hidden;
    box-shadow: 0 12px 30px rgba(0,0,0,0.25);
  }
  .card--front { left: 40px; }
  .card--back { left: 620px; }
  .card__shape { position: absolute; inset: 0; width: 100%; height: 100%; }
  .card__shape path { fill: var(--card-grey); }

  .brand {
    position: absolute;
    display: flex;
    align-items: center;
    gap: 10px;
    font-family: var(--serif);
    font-weight: 700;
    text-transform: uppercase;
    letter-spacing: 1px;
    line-height: 1;
  }
  .brand__mark { border-radius: 50%; flex: none; }
  .brand--front { right: 32px; top: 130px; color: var(--brand-dim); font-size: 15px; }
  .brand--front .brand__mark { width: 26px; height: 26px; background: var(--brand-dim); }
  .brand--back { left: 150px; top: 100px; color: var(--brand-dark); font-size: 24px; }
  .brand--back .brand__mark { width: 44px; height: 44px; background: var(--brand-dark); }

  .person { position: absolute; left: 34px; top: 130px; color: var(--text-light); }
  .person__name { font-size: 21px; font-weight: 700; letter-spacing: 0.3px; }
  .person__role { font-size: 10px; color: var(--text-soft); margin-top: 6px; letter-spacing: 0.5px; }

  .contact { position: absolute; left: 34px; top: 210px; list-style: none; }
  .contact__item {
    display: flex; align-items: center; gap: 12px;
    font-size: 10px; color: var(--text-soft); margin-bottom: 12px;
  }
  .contact__icon {
    width: 18px; height: 18px; background: var(--text-light);
    display: flex; align-items: center; justify-content: center; flex: none;
  }
  .contact__icon svg { width: 12px; height: 12px; }

  .capabilities {
    position: absolute; left: 0; right: 0; bottom: 18px;
    text-align: center; color: var(--text-soft);
    font-size: 10px; line-height: 1.7; letter-spacing: 0.3px;
  }
</style>
</head>
<body>

<section class="card card--front" aria-label="Business card front">
  <svg class="card__shape" viewBox="0 0 540 309" preserveAspectRatio="none" aria-hidden="true">
    <path d="M0 0 H300 C345 0 352 38 346 78 C340 118 382 128 386 170 C390 220 348 245 362 309 H0 Z"/>
  </svg>
  <div class="brand brand--front"><span class="brand__mark"></span>Wombat Devices</div>
  <div class="person">
    <h1 class="person__name">Dr Colin Marsh</h1>
    <p class="person__role">R&amp;D Engineer</p>
  </div>
  <ul class="contact">
    <li class="contact__item">
      <span class="contact__icon">
        <svg viewBox="0 0 12 12"><rect x="1" y="2.5" width="10" height="7" fill="none" stroke="#0a0a0a" stroke-width="1.2"/><path d="M1 2.5 L6 7 L11 2.5" fill="none" stroke="#0a0a0a" stroke-width="1.2"/></svg>
      </span>
      colin@wombatdevicesco.com.au
    </li>
    <li class="contact__item">
      <span class="contact__icon">
        <svg viewBox="0 0 12 12"><rect x="3.5" y="1" width="5" height="10" rx="1" fill="none" stroke="#0a0a0a" stroke-width="1.2"/><circle cx="6" cy="9" r="0.7" fill="#0a0a0a"/></svg>
      </span>
      0427 563 210
    </li>
  </ul>
</section>

<section class="card card--back" aria-label="Business card back">
  <svg class="card__shape" viewBox="0 0 540 309" preserveAspectRatio="none" aria-hidden="true">
    <path d="M70 0 H470 C505 30 478 70 496 110 C512 150 480 190 488 248 H70 C50 210 88 170 62 130 C40 90 78 45 70 0 Z"/>
  </svg>
  <div class="brand brand--back"><span class="brand__mark"></span>Wombat Devices</div>
  <p class="capabilities">
    · Instrumentation for electrical testing · Radar jammers · GPS antenna design<br>
    · Satellite tracking systems · High power lasers
  </p>
</section>

</body>
</html>
```